Business car for dental practice

I have a new logo. Want it use for a new business card design. Hi end dental practice Would like a scan code on it for quick access to my web site and mobile site too. Green and purple are in logo design. Maybe have scan code on back? My website is peterhalvorsenDDS.example
Updates

Lakemont Crest Dental Associates

248 N Fairlawn Ave
Wrenfield, NY 10593
555-318-4072

317 N Wexford Rd. 
Suite 406
Mt. Ardley, NY 10587
555-762-1938

would like to incorporate logo, and addresses of both offices, and I recently saw a business card with a scan box on it which would bring people directly to the web site. if anyone knows how to do that, that could possibly go on the back of the card. (May be something I have to add at printing process) card can be one sided, or two sided.  

Reason: designer is revising for me. has not posted changes yet. hope he does soon!!

Industry/Entity Type

Business

```html
<!DOCTYPE html>
<html lang="en">
<head>
<meta charset="utf-8">
<title>Lakemont Crest Dental Associates – Business Card Concepts</title>
<link href="https://fonts.googleapis.com/css2?family=Arimo:wght@400;700&family=Gelasio:wght@400&display=swap" rel="stylesheet">
<style>
  :root {
    --sheet: #a3a3a3;
    --paper: #ffffff;
    --purple: #5b0f9a;
    --purple-deep: #3f0777;
    --purple-glow: #6a12b3;
    --ink-purple: #4a0a84;
    --green: #4fc400;
    --green-light: #7ee22a;
    --white: #ffffff;
  }
  * { box-sizing: border-box; margin: 0; padding: 0; }
  html, body { width: 853px; height: 1200px; overflow: hidden; }
  body {
    background: var(--sheet);
    font-family: "Arimo", Arial, sans-serif;
    position: relative;
  }
  .card {
    position: absolute;
    width: 382px;
    height: 238px;
    overflow: hidden;
  }
  .card--front { left: 51px; background: var(--paper); }
  .card--back {
    left: 443px;
    background: radial-gradient(ellipse at 40% 45%, var(--purple-glow) 0%, var(--purple) 45%, var(--purple-deep) 100%);
    color: var(--white);
  }
  .row-1 { top: 57px; }
  .row-2 { top: 328px; }
  .row-3 { top: 608px; }
  .row-4 { top: 900px; }

  .brand {
    position: absolute;
    display: flex;
    align-items: center;
    gap: 5px;
    color: var(--ink-purple);
    font-family: "Gelasio", Georgia, serif;
    font-weight: 400;
  }
  .brand__mark {
    width: 24px; height: 24px;
    background: var(--purple);
    flex: none;
  }
  .brand__name { font-size: 23px; line-height: 1; letter-spacing: -0.2px; }
  .brand__sub { display: block; font-size: 9.5px; letter-spacing: 1.6px; margin-top: 2px; text-align: center; }

  .owner { position: absolute; text-align: right; }
  .owner__name { font-size: 11.5px; font-weight: 700; line-height: 1.1; }
  .owner__title { font-size: 5.5px; line-height: 1.2; }
  .owner--light { color: var(--white); }
  .owner--light .owner__name { font-weight: 400; }
  .owner--purple { color: var(--ink-purple); }

  .address { position: absolute; font-size: 8.3px; line-height: 10.6px; white-space: nowrap; }
  .address--light { color: var(--white); }
  .address--purple { color: var(--ink-purple); font-weight: 700; }

  .web-small {
    position: absolute; left: 0; right: 0; top: 207px;
    text-align: center; font-size: 7.5px; color: var(--ink-purple); font-weight: 700;
  }
  .web-rule {
    position: absolute; left: 39px; right: 40px; top: 109px;
    display: flex; align-items: center; gap: 4px;
    font-size: 13.5px; color: var(--white);
  }
  .web-rule::before, .web-rule::after {
    content: ""; flex: 1; height: 1px; background: rgba(255,255,255,0.85);
  }

  .band { position: absolute; left: 0; bottom: 0; width: 382px; height: 18px; display: block; }
  .green-panel {
    position: absolute; left: 226px; top: 0; width: 156px; height: 238px;
    background: radial-gradient(ellipse at 45% 40%, var(--green-light) 0%, var(--green) 70%, #43ad00 100%);
  }
  .divider-v { position: absolute; width: 1.5px; }
  .divider-v--green { background: var(--green); left: 226px; top: 32px; height: 200px; }
  .divider-v--purple { background: var(--ink-purple); left: 198px; top: 165px; height: 42px; }
  .corner { position: absolute; left: 0; bottom: 0; width: 190px; height: 64px; display: block; }
</style>
</head>
<body>

  <!-- Concept 1 -->
  <section class="card card--front row-1">
    <div class="brand" style="left:106px; top:98px;">
      <span class="brand__mark"></span>
      <span><span class="brand__name">Lakemont Crest</span><span class="brand__sub">Dental Associates</span></span>
    </div>
    <p class="web-small">www.lakemontcrest.example</p>
    <svg class="band" viewBox="0 0 382 18" preserveAspectRatio="none">
      <defs>
        <linearGradient id="g1" x1="0" x2="1"><stop offset="0" stop-color="#4fc400"/><stop offset="1" stop-color="#8fe84a"/></linearGradient>
        <linearGradient id="p1" x1="0" x2="1"><stop offset="0" stop-color="#4a0a84"/><stop offset="1" stop-color="#6a2aa8"/></linearGradient>
      </defs>
      <rect width="382" height="18" fill="url(#g1)"/>
      <polygon points="196,18 222,0 382,0 382,18" fill="url(#p1)"/>
    </svg>
  </section>
  <section class="card card--back row-1">
    <div class="owner owner--light" style="right:24px; top:22px;">
      <p class="owner__name">Name of owner</p>
      <p class="owner__title">Designation</p>
    </div>
    <div class="address address--light" style="left:16px; top:136px;">
      Lakemont Crest Dental Associates<br>248 N Fairlawn Ave<br>Wrenfield, NY 10593<br>555-318-4072<br>317 N Wexford Rd.<br>Suite 406<br>Mt. Ardley, NY 10587<br>555-762-1938
    </div>
  </section>

  <!-- Concept 2 -->
  <section class="card card--front row-2">
    <div class="brand" style="left:18px; top:98px;">
      <span class="brand__mark"></span>
      <span><span class="brand__name">Lakemont Crest</span><span class="brand__sub">Dental Associates</span></span>
    </div>
    <div class="green-panel">
      <div class="owner owner--light" style="left:19px; top:30px;">
        <p class="owner__name">Name of owner</p>
        <p class="owner__title">Designation</p>
      </div>
      <div class="address address--light" style="left:19px; top:89px;">
        Lakemont Crest Dental Associates<br>248 N Fairlawn Ave<br>Wrenfield, NY 10593<br>555-318-4072<br>317 N Wexford Rd.<br>Suite 406<br>Mt. Ardley, NY 10587<br>555-762-1938
      </div>
    </div>
  </section>
  <section class="card card--back row-2">
    <p class="web-rule">www.lakemontcrest.example</p>
  </section>

  <!-- Concept 3 -->
  <section class="card card--front row-3">
    <div class="brand" style="left:18px; top:97px;">
      <span class="brand__mark"></span>
      <span><span class="brand__name">Lakemont Crest</span><span class="brand__sub">Dental Associates</span></span>
    </div>
    <span class="divider-v divider-v--green"></span>
    <div class="owner owner--purple" style="left:236px; top:36px;">
      <p class="owner__name">Name of owner</p>
      <p class="owner__title">Designation</p>
    </div>
    <div class="address address--purple" style="left:237px; top:88px;">
      Lakemont Crest Dental Associates<br>248 N Fairlawn Ave<br>Wrenfield, NY 10593<br>555-318-4072<br>317 N Wexford Rd.<br>Suite 406<br>Mt. Ardley, NY 10587<br>555-762-1938
    </div>
    <svg class="corner" viewBox="0 0 190 64" preserveAspectRatio="none">
      <defs>
        <linearGradient id="g3" x1="0" x2="1"><stop offset="0" stop-color="#4fc400"/><stop offset="1" stop-color="#8fe84a"/></linearGradient>
        <linearGradient id="p3" x1="0" x2="1"><stop offset="0" stop-color="#4a0a84"/><stop offset="1" stop-color="#7a22c0"/></linearGradient>
      </defs>
      <polygon points="0,0 186,64 0,64" fill="url(#g3)"/>
      <polygon points="0,0 150,64 0,64" fill="url(#p3)"/>
    </svg>
  </section>
  <section class="card card--back row-3">
    <p class="web-rule">www.lakemontcrest.example</p>
  </section>

  <!-- Concept 4 -->
  <section class="card card--front row-4">
    <div class="owner owner--purple" style="right:15px; top:18px;">
      <p class="owner__name">Name of owner</p>
      <p class="owner__title">Designation</p>
    </div>
    <div class="brand" style="left:95px; top:76px;">
      <span class="brand__mark"></span>
      <span><span class="brand__name">Lakemont Crest</span><span class="brand__sub">Dental Associates</span></span>
    </div>
    <div class="address address--purple" style="left:37px; top:170px;">
      Lakemont Crest Dental Associates<br>248 N Fairlawn Ave<br>Wrenfield, NY 10593<br>555-318-4072
    </div>
    <span class="divider-v divider-v--purple"></span>
    <div class="address address--purple" style="left:261px; top:170px;">
      317 N Wexford Rd.<br>Suite 406<br>Mt. Ardley, NY 10587<br>555-762-1938
    </div>
    <svg class="band" viewBox="0 0 382 18" preserveAspectRatio="none">
      <defs>
        <linearGradient id="g4" x1="0" x2="1"><stop offset="0" stop-color="#4fc400"/><stop offset="1" stop-color="#8fe84a"/></linearGradient>
        <linearGradient id="p4" x1="0" x2="1"><stop offset="0" stop-color="#4a0a84"/><stop offset="1" stop-color="#6a2aa8"/></linearGradient>
      </defs>
      <rect width="382" height="18" fill="url(#g4)"/>
      <polygon points="172,18 198,0 382,0 382,18" fill="url(#p4)"/>
    </svg>
  </section>
  <section class="card card--back row-4">
    <p class="web-rule">www.lakemontcrest.example</p>
  </section>

</body>
</html>
```